依頼詳細
タイ古式マッサージの看板ポスターを作成依頼をお願いします。
サイズはA2サイズです。よろしくお願いします。
例文は添付致します。
記載項目
店舗名、電話番号、ロゴ
希望イメージ
シンプル 複雑
単色 カラフル
暗い 明るい
日常 高級
遊び心 厳粛
未来的 伝統的
女性的 男性的
希望する色
赤系、茶系、緑系、グレー系
納品ファイル
• 高解像度JPG (.jpg)
• イラストレーター形式 (.ai)
補足説明
スタンド看板にしますのでA2サイズでなく原稿サイズ435x940でお願いします。
すみませんがよろしくお願いします。

■ 選んだ理由

色がとてもいいです!! パッと見て目立つしわかりやすいと思いました。
ありがとうございました。

■ 提案者全員のお礼・コメント

この度は、皆様方にご提案頂きまして誠にありがとうございました。
また、何かございましたらよろしくお願いします。
ありがとうございました。

```html
<!DOCTYPE html>
<html lang="ja">
<head>
<meta charset="utf-8">
<title>タイ古式マッサージ スタンド看板</title>
<link rel="stylesheet" href="https://fonts.googleapis.com/css2?family=Noto+Sans+JP:wght@500;700;900&family=Noto+Serif+JP:wght@600;700;900&display=swap">
<style>
  :root {
    --red-top: #e23a1b;
    --orange-hot: #ef7420;
    --orange: #f5a324;
    --amber: #f3b42a;
    --lime: #b6cb38;
    --green: #78bd3a;
    --title-red: #d7261a;
    --deep-red: #a8221a;
    --copy-orange: #e9751e;
    --white: #ffffff;
    --ink: #3a2412;
    --ornament-red: #b8241a;
    --ornament-green: #5f9f2a;
  }
  * { margin: 0; padding: 0; box-sizing: border-box; }
  html, body { width: 1200px; height: 2332px; overflow: hidden; background: #ffffff; }
  .poster {
    position: relative;
    width: 1200px;
    height: 2332px;
    overflow: hidden;
    background: linear-gradient(180deg,
      var(--red-top) 0%,
      var(--orange-hot) 22%,
      var(--orange) 50%,
      var(--amber) 70%,
      var(--lime) 85%,
      var(--green) 100%);
    font-family: "Noto Serif JP", serif;
  }
  .ornament { position: absolute; }
  .ornament--top-left {
    left: 0; top: 0; width: 300px; height: 250px;
    background: radial-gradient(ellipse at 20% 20%, rgba(184,36,26,0.75) 0%, rgba(184,36,26,0.35) 45%, rgba(184,36,26,0) 75%);
  }
  .ornament--top-right {
    right: 0; top: 0; width: 300px; height: 250px;
    background: radial-gradient(ellipse at 80% 20%, rgba(184,36,26,0.75) 0%, rgba(184,36,26,0.35) 45%, rgba(184,36,26,0) 75%);
  }
  .ornament--bottom-left {
    left: 0; bottom: 0; width: 320px; height: 420px;
    background: radial-gradient(ellipse at 25% 70%, rgba(95,159,42,0.7) 0%, rgba(95,159,42,0.3) 45%, rgba(95,159,42,0) 75%);
  }
  .ornament--bottom-right {
    right: 0; bottom: 0; width: 320px; height: 420px;
    background: radial-gradient(ellipse at 75% 70%, rgba(95,159,42,0.7) 0%, rgba(95,159,42,0.3) 45%, rgba(95,159,42,0) 75%);
  }

  .concern {
    position: absolute;
    left: 150px; top: 215px; width: 900px; height: 190px;
    background: var(--white);
    border-radius: 95px;
    display: flex; flex-direction: column; justify-content: center; align-items: center;
    color: var(--title-red);
    font-weight: 700;
    font-size: 52px;
    line-height: 1.4;
    letter-spacing: 2px;
  }

  .title {
    position: absolute;
    left: 0; top: 440px; width: 1200px;
    text-align: center;
    color: var(--title-red);
    font-weight: 900;
    font-size: 196px;
    line-height: 1.0;
    letter-spacing: 6px;
    -webkit-text-stroke: 18px var(--white);
    paint-order: stroke fill;
  }
  .title span { display: block; }
  .title span + span { margin-top: 14px; }

  .voices {
    position: absolute;
    left: 0; top: 905px; width: 1200px;
    text-align: center;
    color: var(--deep-red);
    font-weight: 600;
    font-size: 42px;
    line-height: 1.5;
  }

  .benefit {
    position: absolute;
    left: 190px; top: 1128px; width: 830px; height: 272px;
    background: var(--white);
    border-radius: 60px;
    display: flex; flex-direction: column; justify-content: center; align-items: center;
    color: var(--copy-orange);
    font-family: "Noto Sans JP", sans-serif;
    font-weight: 700;
    font-size: 46px;
    line-height: 1.5;
    text-align: center;
  }

  .description {
    position: absolute;
    left: 168px; top: 1455px; width: 900px;
    color: var(--ink);
    font-family: "Noto Sans JP", sans-serif;
    font-weight: 500;
    font-size: 27px;
    line-height: 1.62;
    text-align: justify;
  }

  .prices {
    position: absolute;
    left: 168px; top: 1740px; width: 900px;
    color: var(--white);
    font-family: "Noto Sans JP", sans-serif;
    font-weight: 700;
    list-style: none;
  }
  .price {
    display: flex; align-items: baseline;
    font-size: 82px;
    line-height: 1.45;
  }
  .price__time { width: 250px; }
  .price__amount { }
  .price__tax { font-size: 44px; margin-left: 6px; }

  .brand {
    position: absolute;
    left: 0; top: 1990px; width: 1200px;
    text-align: center;
    color: var(--white);
    font-family: "Noto Serif JP", serif;
    font-weight: 700;
    font-size: 96px;
    letter-spacing: 10px;
    line-height: 1;
  }

  .contact {
    position: absolute;
    left: 0; top: 2140px; width: 1200px;
    display: flex; justify-content: center; align-items: center; gap: 20px;
    color: var(--white);
    font-family: "Noto Sans JP", sans-serif;
    font-weight: 700;
    font-size: 78px;
    line-height: 1;
    letter-spacing: 2px;
  }
  .contact__icon { width: 72px; height: 72px; }
</style>
</head>
<body>
<main class="poster">
  <div class="ornament ornament--top-left" role="img" aria-label="左上の赤い唐草模様の飾り"></div>
  <div class="ornament ornament--top-right" role="img" aria-label="右上の赤い唐草模様の飾り"></div>
  <div class="ornament ornament--bottom-left" role="img" aria-label="左下の緑の唐草模様の飾り"></div>
  <div class="ornament ornament--bottom-right" role="img" aria-label="右下の緑の唐草模様の飾り"></div>

  <p class="concern">
    <span>辛い首こりや肩こり</span>
    <span>体の疲れがヒドイあなたに</span>
  </p>

  <h1 class="title">
    <span>タイ古式</span>
    <span>マッサージ</span>
  </h1>

  <p class="voices">
    『気づいたら、寝ていた』<br>
    『ビックリするほど、体が軽くなった』
  </p>

  <p class="benefit">
    <span>全身をほぐしますので、</span>
    <span>クイックマッサージにはない効果が</span>
    <span>実感できます。</span>
  </p>

  <p class="description">
    別名『二人で行うヨガ』と言われ、もむ、押すだけでなくストレッチ施術で血行を促しながら筋肉の柔軟性を高めていきます。何だかプロレス技を掛けられているようなストレッチですが、ゆっくりと体がほぐされていくので痛くなく、『世界で一番気持ちいいマッサージ』と言われています。
  </p>

  <ul class="prices">
    <li class="price"><span class="price__time">30分</span><span class="price__amount">3,500円</span><span class="price__tax">(税込)</span></li>
    <li class="price"><span class="price__time">60分</span><span class="price__amount">5,900円</span><span class="price__tax">(税込)</span></li>
  </ul>

  <p class="brand">SORANA</p>

  <p class="contact">
    <svg class="contact__icon" viewBox="0 0 24 24" aria-hidden="true">
      <path fill="#ffffff" d="M6.6 10.8c1.4 2.8 3.8 5.1 6.6 6.6l2.2-2.2c.3-.3.7-.4 1-.2 1.1.4 2.3.6 3.6.6.6 0 1 .4 1 1V20c0 .6-.4 1-1 1C10.6 21 3 13.4 3 4c0-.6.4-1 1-1h3.5c.6 0 1 .4 1 1 0 1.3.2 2.5.6 3.6.1.3 0 .7-.2 1l-2.3 2.2z"/>
    </svg>
    <span class="contact__tel">03-5555-0142</span>
  </p>
</main>
</body>
</html>
```